Food home delivery flyer to attract new customers and drive web traffic

We need a flyer for Pantrelo Home Delivery for our door to door leaflet drop. The aim of our marketing is to attract new customers by driving traffic to our website and raise awareness of our service.

We want the flyer in A5, double sided, and in colour. This campaign will be primarily in print, but we need a PDF option also.

Please visit www.pantrelohomedelivery.example to obtain a real feel of who we are and what we do.

The flyer should contain the Pantrelo Home Delivery logo, with our images to compliment our service and what we offer. All are attached to this brief, along with what wording we expect to be included in the flyer.

The main points we need to shout about are:
Sourcing fresh produce from local growers
Partnering with local businesses
Friendly team offering superior customer service
Fast, safe home delivery
Sustainable business

```html
<!DOCTYPE html>
<html lang="en">
<head>
<meta charset="utf-8">
<title>Pantrelo Home Delivery – A5 Flyer Presentation</title>
<link href="https://fonts.googleapis.com/css2?family=Open+Sans:wght@400;600;700;800&display=swap" rel="stylesheet">
<style>
  :root{
    --forest:#14622f;
    --forest-deep:#0f5526;
    --lime:#b3d443;
    --lime-soft:#c6e06a;
    --brown:#5b3f2a;
    --card:#d7b98c;
    --card-dark:#c9a877;
    --white:#ffffff;
    --ink:#3b3b3b;
    --page-shadow:0 0 8px rgba(0,0,0,.25);
  }
  *{box-sizing:border-box;margin:0;padding:0}
  html,body{width:1200px;height:1200px;overflow:hidden;background:var(--white)}
  body{position:relative;font-family:"Open Sans",Arial,sans-serif;color:var(--forest)}
  .page{position:absolute;top:42px;width:547px;height:766px;background:var(--lime);box-shadow:var(--page-shadow);overflow:hidden}
  .page--front{left:35px}
  .page--back{left:621px}
  .abs{position:absolute}
  .center{left:0;right:0;text-align:center}

  /* brand */
  .brand-head{top:0;left:0;right:0;background:var(--white)}
  .page--front .brand-head{height:102px}
  .page--back .brand-head{height:91px}
  .brand{position:absolute;left:0;right:0;text-align:center}
  .brand__name{display:block;font-weight:600;font-size:38px;line-height:1;color:var(--forest);letter-spacing:.5px}
  .brand__tag{display:block;font-size:12px;color:var(--ink);margin-top:4px;padding-left:60px}
  .brand__tag::before{content:"";display:inline-block;width:50px;height:1px;background:var(--ink);vertical-align:middle;margin-right:4px}
  .page--front .brand{top:33px}
  .page--back .brand{top:24px}

  /* front headline band */
  .headline-band{top:102px;left:0;right:0;height:92px;background:var(--forest);text-align:center;padding-top:9px}
  .headline-band__main{font-weight:800;font-size:25.5px;line-height:1.05;color:var(--lime)}
  .headline-band__sub{font-weight:800;font-size:16px;line-height:1.2;color:var(--lime)}
  .headline-band__note{font-weight:600;font-size:15px;line-height:1.35;color:var(--white)}
  .scallop-down{left:0;right:0;height:6px;background:radial-gradient(circle at 6px 0,var(--forest) 5.5px,transparent 6px) repeat-x;background-size:12px 6px}
  .scallop-brown{left:0;right:0;height:7px;background:radial-gradient(circle at 7px 0,var(--brown) 6.5px,transparent 7px) repeat-x;background-size:14px 7px}

  .photo{position:absolute}
  .photo--platter{top:194px;left:0;right:0;height:330px;background:radial-gradient(ellipse at 45% 45%,#efe6da 0%,#d9c7b3 55%,#b98a66 100%)}
  .photo--produce{top:91px;left:0;right:0;height:230px;background:linear-gradient(120deg,#e0772e 0%,#c9423a 30%,#8fb041 55%,#e2b54a 75%,#b8303b 100%)}
  .curve{position:absolute;left:0;width:547px}

  /* offer */
  .offer-bar{top:508px;left:138px;width:374px;height:70px;background:var(--forest)}
  .offer-bar__title{position:absolute;top:6px;left:20px;font-weight:700;font-size:21.5px;color:var(--white);white-space:nowrap}
  .offer-bar__code{position:absolute;top:35px;left:3px;width:352px;height:26px;background:var(--white);font-size:14px;line-height:26px;padding-left:15px;color:var(--forest-deep);white-space:nowrap}
  .offer-bar__code b{font-weight:800}
  .offer-badge{top:490px;left:38px;width:104px;height:104px;border-radius:50%;background:var(--forest);border:3px solid var(--lime-soft);color:var(--white);text-align:center;padding-top:12px}
  .offer-badge__lead{font-size:13px;line-height:1}
  .offer-badge__big{font-weight:800;font-size:29px;line-height:1}
  .offer-strap{top:594px;font-size:13px;line-height:1.25;font-weight:600;color:var(--forest)}

  /* shared footer */
  .order-band{top:630px;left:0;right:0;height:61px;background:var(--brown);color:var(--white);text-align:center;padding-top:5px}
  .order-band__line{display:flex;justify-content:center;align-items:center;gap:4px;font-size:12.5px;white-space:nowrap;height:26px}
  .order-band__url{font-weight:700;font-size:20.5px;color:var(--lime);margin-left:3px}
  .order-band__note{font-size:12.5px;line-height:1.2;padding-left:20px}
  .order-band__icon{flex:none;margin-top:8px}
  .call-pill{top:681px;left:40px;width:214px;height:52px;background:var(--forest);border-radius:10px;box-shadow:0 3px 4px rgba(0,0,0,.25);color:var(--white);text-align:center;padding-top:4px}
  .call-pill__small{font-weight:600;font-size:12.5px;line-height:1.2}
  .call-pill__big{font-weight:700;font-size:25px;line-height:1.15}
  .call-phone{top:707px;left:275px;display:flex;align-items:center;gap:12px}
  .call-phone__number{font-weight:800;font-size:30px;color:var(--forest);letter-spacing:.3px}

  /* back */
  .intro{top:337px;left:42px;width:243px;color:var(--forest);text-align:justify}
  .intro__lead{font-weight:700;font-size:14.5px;line-height:1.2}
  .intro__lead strong{font-size:21.5px;font-weight:800}
  .intro p{font-size:12.3px;line-height:1.22;font-weight:600;margin-top:2px}
  .intro p + p{margin-top:12px}
  .eco-panel{top:250px;left:304px;width:201px;height:266px;background:linear-gradient(160deg,var(--card),var(--card-dark))}
  .eco-panel__text{position:absolute;top:140px;left:2px;right:2px;text-align:center;font-size:12px;line-height:15px;color:var(--forest);white-space:nowrap}
  .eco-panel__text b{font-weight:700;font-size:13px;line-height:16px}
  .eco-seal{top:183px;left:301px;width:204px;height:204px;border-radius:50%;background:radial-gradient(circle,#fff 60%,#eef5dc 100%);border:8px solid var(--forest);text-align:center;color:var(--forest);font-weight:800;padding-top:28px}
  .eco-seal span{display:block;line-height:1.02}
  .s1{font-size:30px}.s2{font-size:26px}.s3{font-size:22px}.s4{font-size:18px}.s5{font-size:30px}
  .thumb{top:516px;height:107px;position:absolute}
  .thumb--pies{left:0;width:173px;background:linear-gradient(135deg,#8a6d3b,#c3a060 50%,#6f8c3a)}
  .thumb--pizza{left:184px;width:152px;background:radial-gradient(circle,#d65a3a,#b2402c 60%,#7a5a3c)}
  .thumb--box{left:347px;width:200px;background:linear-gradient(120deg,#c7a77a,#6a9a3a 40%,#d24a3a 70%,#e0c04a)}

  /* presentation labels */
  .label{position:absolute;font-weight:600;font-size:28px;color:var(--forest);letter-spacing:.3px}
  .label--front{left:36px;top:820px}
  .label--back{left:622px;top:830px}
  .detail{position:absolute;left:619px;top:973px;width:141px;height:192px;background:linear-gradient(160deg,var(--card),var(--card-dark));box-shadow:var(--page-shadow)}
  .detail__seal{position:absolute;left:0;top:-35px;width:141px;height:141px;border-radius:50%;background:radial-gradient(circle,#fff 62%,#eef5dc 100%);border:5px solid var(--forest);text-align:center;font-weight:800;color:var(--forest);padding-top:20px}
  .detail__seal span{display:block;line-height:1.02}
  .d1{font-size:20px}.d2{font-size:17px}.d3{font-size:14px}.d4{font-size:12px}.d5{font-size:20px}
  .detail__text{position:absolute;top:114px;left:3px;right:3px;text-align:center;font-size:8.6px;line-height:1.22;color:var(--forest)}
  .detail__text b{font-weight:700}
  .callout-arrow{position:absolute;left:746px;top:1056px}
  .callout-note{position:absolute;left:845px;top:1012px;width:330px;font-size:21.5px;line-height:1.2;color:var(--forest)}
</style>
</head>
<body>

<!-- FRONT -->
<section class="page page--front" aria-label="Flyer front">
  <header class="abs brand-head">
    <div class="brand"><span class="brand__name">Pantrelo</span><span class="brand__tag">home delivery</span></div>
  </header>

  <div class="abs headline-band">
    <div class="headline-band__main">LOVINGLY PICKED KENTISH FOOD</div>
    <div class="headline-band__sub">SAFELY DELIVERED FROM OUR FARM TO YOUR HOME</div>
    <div class="headline-band__note">BY PASSIONATE LOCAL PEOPLE WHO CARE.</div>
  </div>
  <div class="photo photo--platter" role="img" aria-label="Overhead photo of a sharing platter: bruschetta, olives, feta, chillies and cured meat rolls"></div>
  <div class="abs scallop-down" style="top:194px"></div>
  <svg class="curve" style="top:420px" height="110" viewBox="0 0 547 110" aria-hidden="true">
    <path d="M0 0 C60 95 200 105 300 98 C420 90 500 50 547 0 L547 110 L0 110Z" fill="var(--lime)"/>
    <path d="M0 0 C60 95 200 105 300 98 C420 90 500 50 547 0" fill="none" stroke="#fff" stroke-width="4"/>
  </svg>

  <div class="abs offer-bar">
    <div class="offer-bar__title">ALL YOUR ORDERS IN JULY</div>
    <div class="offer-bar__code">Enter Code <b>LOCALTOWYE</b> at the Checkout</div>
  </div>
  <div class="abs offer-badge">
    <div class="offer-badge__lead">Enjoy</div>
    <div class="offer-badge__big">25%</div>
    <div class="offer-badge__big">OFF</div>
  </div>
  <div class="abs center offer-strap">Avoid the Supermarkets and Enjoy a Unique and Balanced Food<br>Experience with Provenance.</div>

  <div class="abs order-band">
    <div class="order-band__line">
      <svg class="order-band__icon" width="30" height="26" viewBox="0 0 30 26" aria-hidden="true"><rect x="3" y="6" width="15" height="20" rx="7.5" fill="var(--lime)"/><line x1="10.5" y1="7" x2="10.5" y2="13" stroke="var(--brown)" stroke-width="1.5"/><path d="M10.5 6 C12 1 20 0 27 3" stroke="var(--lime)" stroke-width="2" fill="none"/></svg>
      <span>Order Online at</span><span class="order-band__url">www.pantrelohomedelivery.example</span>
    </div>
    <div class="order-band__note">for Fast Contactless Next Day Delivery.</div>
  </div>
  <div class="abs scallop-brown" style="top:691px"></div>
  <div class="abs call-pill"><div class="call-pill__small">CALL OUR FRIENDLY TEAM</div><div class="call-pill__big">AT THE FARM</div></div>
  <div class="abs call-phone">
    <svg width="28" height="28" viewBox="0 0 28 28" aria-hidden="true"><circle cx="14" cy="14" r="14" fill="var(--forest)"/><path d="M9 7 l3 0 l1.5 4 l-2 1.5 a9 9 0 0 0 4 4 l1.5-2 l4 1.5 l0 3 a2 2 0 0 1-2 2 a13 13 0 0 1-12-12 a2 2 0 0 1 2-2z" fill="var(--lime)"/></svg>
    <span class="call-phone__number">01632 960418</span>
  </div>
</section>

<!-- BACK -->
<section class="page page--back" aria-label="Flyer back">
  <header class="abs brand-head">
    <div class="brand"><span class="brand__name">Pantrelo</span><span class="brand__tag">home delivery</span></div>
  </header>
  <div class="photo photo--produce" role="img" aria-label="Photo of fresh mixed vegetables and fruit: carrots, apples, peppers, tomatoes, potatoes"></div>
  <svg class="curve" style="top:230px" height="100" viewBox="0 0 547 100" aria-hidden="true">
    <path d="M0 20 C60 95 160 110 280 70 C380 40 480 50 547 0 L547 100 L0 100Z" fill="var(--lime)"/>
    <path d="M0 20 C60 95 160 110 280 70 C380 40 480 50 547 0" fill="none" stroke="#fff" stroke-width="5"/>
  </svg>

  <div class="abs intro">
    <div class="intro__lead"><strong>Pantrelo</strong> Brings You the Very Best Producers and Growers</div>
    <p>from The Garden of England to Deliver You a Delicious Choice for All Your Dining Needs.</p>
    <p>From fresh produce boxes, handmade picnic boxes, fresh Kentish berry boxes to the finest local beer and wines – we’ve got it covered.</p>
  </div>

  <div class="abs eco-panel">
    <div class="eco-panel__text"><b>Using environmentally<br>conscious practices and<br>minimal packaging,</b><br>working hand in hand with<br>reduced food miles brings you<br>peace of mind with our efforts<br>for a sustainable future.</div>
  </div>
  <div class="abs eco-seal"><span class="s1">START</span><span class="s2">ENJOYING</span><span class="s3">FOOD WITH</span><span class="s4">PROVENANCE</span><span class="s5">NOW!</span></div>

  <div class="thumb thumb--pies" role="img" aria-label="Photo of handmade pies and roasted vegetables"></div>
  <div class="thumb thumb--pizza" role="img" aria-label="Photo of a tomato and basil pizza"></div>
  <div class="thumb thumb--box" role="img" aria-label="Photo of a fresh produce box with eggs, fruit and vegetables"></div>

  <div class="abs order-band">
    <div class="order-band__line">
      <svg class="order-band__icon" width="30" height="26" viewBox="0 0 30 26" aria-hidden="true"><rect x="3" y="6" width="15" height="20" rx="7.5" fill="var(--lime)"/><line x1="10.5" y1="7" x2="10.5" y2="13" stroke="var(--brown)" stroke-width="1.5"/><path d="M10.5 6 C12 1 20 0 27 3" stroke="var(--lime)" stroke-width="2" fill="none"/></svg>
      <span>Order Online at</span><span class="order-band__url">www.pantrelohomedelivery.example</span>
    </div>
    <div class="order-band__note">for Fast Contactless Next Day Delivery.</div>
  </div>
  <div class="abs scallop-brown" style="top:691px"></div>
  <div class="abs call-pill"><div class="call-pill__small">CALL OUR FRIENDLY TEAM</div><div class="call-pill__big">AT THE FARM</div></div>
  <div class="abs call-phone">
    <svg width="28" height="28" viewBox="0 0 28 28" aria-hidden="true"><circle cx="14" cy="14" r="14" fill="var(--forest)"/><path d="M9 7 l3 0 l1.5 4 l-2 1.5 a9 9 0 0 0 4 4 l1.5-2 l4 1.5 l0 3 a2 2 0 0 1-2 2 a13 13 0 0 1-12-12 a2 2 0 0 1 2-2z" fill="var(--lime)"/></svg>
    <span class="call-phone__number">01632 960418</span>
  </div>
</section>

<div class="label label--front">FRONT PAGE</div>
<div class="label label--back">BACK PAGE</div>

<div class="detail">
  <div class="detail__seal"><span class="d1">START</span><span class="d2">ENJOYING</span><span class="d3">FOOD WITH</span><span class="d4">PROVENANCE</span><span class="d5">NOW!</span></div>
  <div class="detail__text"><b>Using environmentally conscious practices and minimal packaging,</b><br>working hand in hand with reduced food miles brings you peace of mind with our efforts for a sustainable future.</div>
</div>
<svg class="callout-arrow" width="88" height="30" viewBox="0 0 88 30" aria-hidden="true"><line x1="0" y1="15" x2="62" y2="15" stroke="#e01b1b" stroke-width="2"/><path d="M60 0 L88 15 L60 30Z" fill="#e01b1b"/></svg>
<p class="callout-note">This section is about using environmentally packaging. Therefore, I use a card board texture background to indicate environmentally packaging.</p>

</body>
</html>
```